Meridale Crest Advisors – Franchise Growth & Development Presentation

Meridale Crest Advisors is an outsourced franchise sales organization (FSO) that helps franchisors grow their franchise systems without the expense and risk of hiring an internal franchise development team.

We are seeking a professional PowerPoint presentation that will be used to present our services to franchisors, franchise executives, founders, and growth-stage franchise brands.

The presentation should communicate the value of partnering with Meridale Crest Advisors, including:

• Fractional franchise sales team versus hiring internal staff
• 30+ years of franchise industry experience
• 550+ franchise sales successes
• Immediate access to established franchise broker relationships
• Proven franchise development processes
• Franchise growth strategy and enterprise value creation
• Potential private equity and exit opportunities through franchise expansion

The presentation should feel like a modern consulting, investment, or growth strategy presentation rather than a typical sales brochure. We want strong visual storytelling, custom infographics, professional diagrams, and clean business-oriented design.

The audience includes business owners, franchise founders, franchise executives, and investors who are evaluating growth strategies for their franchise systems.

Target Market(s)

Primary Audience: Emerging franchisors Growth-stage franchise brands Franchise founders Franchise CEOs Franchise presidents Franchise development executives Secondary Audience: Private equity firms Franchise investors Strategic buyers Franchise consultants

Industry/Entity Type

Franchise Development, Private Equity / Business Expansion

Font styles to use
Other font styles liked:
• Use Montserrat for titles and Open Sans for body text.

Requirements
Must have
• Modern professional business design Consistent branding throughout Custom infographics Comparison graphics Broker network ecosystem graphic Enterprise value graphic Easy-to-read charts and visuals Editable PowerPoint format Professional iconography. www.meridalecrestadvisors.example as reference for colors
Nice to have
• Franchise-related imagery Subtle growth-themed visuals Timeline graphics Data visualization Private equity / valuation style graphics
Should not have
• Cartoon graphics Clip art Overly busy slides Stock-template appearance Bright neon colors Handwritten fonts Excessive text on slides Juvenile or playful design elements

```html
<!DOCTYPE html>
<html lang="en">
<head>
<meta charset="utf-8">
<title>Meridale Crest Advisors – Presentation Overview</title>
<link rel="stylesheet" href="https://fonts.googleapis.com/css2?family=Montserrat:wght@500;600;700;800&family=Open+Sans:wght@400;600;700&display=swap">
<style>
:root{
  --navy:#0f1b33;
  --navy-2:#1c2a48;
  --gold:#a87a3d;
  --gold-light:#d2ac72;
  --ink:#1e2433;
  --muted:#5b6272;
  --paper:#ffffff;
  --cream:#f6f2ec;
  --line:#e3ddd3;
  --ice:#dfe7f1;
}
*{box-sizing:border-box;margin:0;padding:0}
html,body{width:1200px;height:942px;overflow:hidden;background:#fff}
body{position:relative;font-family:"Open Sans",sans-serif;color:var(--ink)}
.slide{position:absolute;width:261px;height:148px;background:var(--paper);overflow:hidden;box-shadow:0 1px 4px rgba(0,0,0,.18)}
.foot{position:absolute;left:0;right:0;bottom:0;height:10px;background:var(--navy);color:#fff;font-size:3.6px;display:flex;align-items:center;justify-content:space-between;padding:0 5px}
.foot .url{display:flex;align-items:center;gap:2px}
.foot .url svg{width:5px;height:5px;stroke:#fff;fill:none;stroke-width:1.6}
.foot .page{background:var(--gold);height:10px;display:flex;align-items:center;padding:0 4px;margin-right:-5px}
.brand{position:absolute;top:5px;right:6px;display:flex;align-items:center;gap:2px;font-family:"Montserrat",sans-serif;font-weight:700;font-size:4px;color:var(--navy);line-height:1.1;width:40px}
.brand::before{content:"";width:6px;height:6px;border-radius:50%;background:var(--gold);flex:none}
.title{position:absolute;font-family:"Montserrat",sans-serif;font-weight:700;font-size:8px;line-height:1.2;color:var(--navy)}
.title .g{color:var(--gold)}
.sm{font-size:3.6px;line-height:1.35;color:var(--ink)}
.lbl{font-family:"Montserrat",sans-serif;font-weight:600;font-size:3.2px;text-align:center;line-height:1.25;color:var(--ink);text-transform:uppercase}
.photo{position:absolute}
.dot{border-radius:50%;background:var(--navy);flex:none;display:flex;align-items:center;justify-content:center;color:#fff}
.dot.gold{background:var(--gold)}
.ring{border-radius:50%;border:.8px solid var(--gold);background:#fff;flex:none;display:flex;align-items:center;justify-content:center;color:var(--navy)}
.ring.navy{border-color:var(--navy)}
.dot svg,.ring svg{width:60%;height:60%;fill:none;stroke:currentColor;stroke-width:1.7;stroke-linecap:round;stroke-linejoin:round}
.row{display:flex;align-items:center;gap:4px}
ul.list{list-style:none}
.steps{position:absolute;left:9px;top:60px;width:243px;display:flex;justify-content:space-between;align-items:flex-start}
.step{width:28px;text-align:center}
.step .ring{width:24px;height:24px;margin:0 auto;border-width:1.2px;border-color:var(--navy);position:relative}
.step .num{position:absolute;top:-4.5px;left:50%;margin-left:-3.5px;width:7px;height:7px;border-radius:50%;background:var(--navy);color:#fff;font-size:3.5px;line-height:7px;font-weight:700}
.step .lbl{text-transform:none;margin-top:4px}
.arrow{width:6px;height:24px;display:flex;align-items:center}
.arrow svg{width:6px;height:6px;fill:none;stroke:var(--gold);stroke-width:2.5}
.svc{text-align:center}
.svc .ring{width:22px;height:22px;margin:0 auto;border-color:var(--navy)}
.svc .lbl{text-transform:none;margin-top:3px}
</style>
</head>
<body>

<svg width="0" height="0" style="position:absolute">
  <defs>
    <symbol id="i-people" viewBox="0 0 24 24"><circle cx="9" cy="8" r="3"/><path d="M3 19c0-3.5 3-5.5 6-5.5s6 2 6 5.5"/><circle cx="17" cy="9" r="2.5"/><path d="M15.5 13.5c3 0 5.5 1.5 5.5 5"/></symbol>
    <symbol id="i-doc" viewBox="0 0 24 24"><path d="M6 3h9l4 4v14H6z"/><path d="M14 3v5h5M9 12h7M9 16h7"/></symbol>
    <symbol id="i-check" viewBox="0 0 24 24"><circle cx="12" cy="12" r="9"/><path d="M8 12l3 3 5-6"/></symbol>
    <symbol id="i-chart" viewBox="0 0 24 24"><path d="M4 20h16M7 17v-5M12 17V8M17 17V5"/></symbol>
    <symbol id="i-cap" viewBox="0 0 24 24"><path d="M2 9l10-5 10 5-10 5z"/><path d="M6 11v5c3 2 9 2 12 0v-5"/></symbol>
    <symbol id="i-cal" viewBox="0 0 24 24"><rect x="4" y="5" width="16" height="15" rx="1"/><path d="M4 10h16M8 3v4M16 3v4M9 15l2 2 4-4"/></symbol>
    <symbol id="i-hand" viewBox="0 0 24 24"><path d="M2 11l4-4 4 2 4-2 4 2 4 4"/><path d="M6 12l4 4 2-1 2 1 4-4"/><path d="M10 9l3 3"/></symbol>
    <symbol id="i-shield" viewBox="0 0 24 24"><path d="M12 3l8 3v6c0 5-4 8-8 9-4-1-8-4-8-9V6z"/><path d="M8.5 12l2.5 2.5 4.5-5"/></symbol>
    <symbol id="i-chat" viewBox="0 0 24 24"><path d="M4 5h16v10H9l-5 4z"/><path d="M8 10h8"/></symbol>
    <symbol id="i-gear" viewBox="0 0 24 24"><circle cx="12" cy="12" r="3"/><path d="M12 3v3M12 18v3M3 12h3M18 12h3M5.6 5.6l2.1 2.1M16.3 16.3l2.1 2.1M5.6 18.4l2.1-2.1M16.3 7.7l2.1-2.1"/></symbol>
    <symbol id="i-target" viewBox="0 0 24 24"><circle cx="12" cy="12" r="9"/><circle cx="12" cy="12" r="5"/><circle cx="12" cy="12" r="1"/></symbol>
    <symbol id="i-bulb" viewBox="0 0 24 24"><path d="M9 18h6M10 21h4"/><path d="M12 3a6 6 0 0 0-3.5 11c.5.5.5 1 .5 2h6c0-1 0-1.5.5-2A6 6 0 0 0 12 3z"/></symbol>
    <symbol id="i-dollar" viewBox="0 0 24 24"><circle cx="12" cy="12" r="9"/><path d="M15 9c-1-1.5-6-1.5-6 1s6 1.5 6 4-5 2.5-6 1M12 6v12"/></symbol>
    <symbol id="i-clock" viewBox="0 0 24 24"><circle cx="12" cy="12" r="9"/><path d="M12 7v5l3 2"/></symbol>
    <symbol id="i-search" viewBox="0 0 24 24"><circle cx="11" cy="11" r="6"/><path d="M16 16l5 5"/></symbol>
    <symbol id="i-funnel" viewBox="0 0 24 24"><path d="M3 4h18l-7 8v7l-4 2v-9z"/></symbol>
    <symbol id="i-mail" viewBox="0 0 24 24"><rect x="3" y="6" width="18" height="12"/><path d="M3 7l9 6 9-6"/></symbol>
    <symbol id="i-headset" viewBox="0 0 24 24"><path d="M4 14v-2a8 8 0 0 1 16 0v2"/><rect x="3" y="13" width="4" height="6"/><rect x="17" y="13" width="4" height="6"/></symbol>
    <symbol id="i-star" viewBox="0 0 24 24"><path d="M12 3l2.6 6 6.4.5-5 4 1.6 6.5-5.6-3.5-5.6 3.5 1.6-6.5-5-4 6.4-.5z"/></symbol>
    <symbol id="i-trend" viewBox="0 0 24 24"><path d="M3 18l6-6 4 4 8-8M15 8h6v6"/></symbol>
    <symbol id="i-monitor" viewBox="0 0 24 24"><rect x="3" y="4" width="18" height="12"/><path d="M8 20h8M12 16v4"/></symbol>
    <symbol id="i-trophy" viewBox="0 0 24 24"><path d="M7 4h10v4a5 5 0 0 1-10 0z"/><path d="M12 13v4M8 20h8M7 6H4c0 3 1.5 4 3 4M17 6h3c0 3-1.5 4-3 4"/></symbol>
    <symbol id="i-network" viewBox="0 0 24 24"><circle cx="12" cy="5" r="2.5"/><circle cx="5" cy="18" r="2.5"/><circle cx="19" cy="18" r="2.5"/><path d="M11 7.5l-5 8M13 7.5l5 8M7.5 18h9"/></symbol>
    <symbol id="i-building" viewBox="0 0 24 24"><path d="M4 21V5h9v16M13 9h7v12M3 21h18M7 8h3M7 12h3M7 16h3M16 13h1M16 17h1"/></symbol>
    <symbol id="i-globe" viewBox="0 0 24 24"><circle cx="12" cy="12" r="9"/><ellipse cx="12" cy="12" rx="4" ry="9"/><path d="M3 12h18"/></symbol>
  </defs>
</svg>

<!-- 01 Cover -->
<section class="slide" style="left:34px;top:36px">
  <div class="photo" role="img" aria-label="Sunset city skyline with a suspension bridge" style="left:120px;top:0;width:141px;height:148px;background:linear-gradient(160deg,#3a4a63 0%,#c7925a 45%,#5c4b3c 100%)"></div>
  <svg style="position:absolute;left:0;top:0" width="261" height="148"><polygon points="100,0 190,0 120,148 60,148" fill="#fff"/><polygon points="150,0 190,0 140,40" fill="var(--navy)"/><polygon points="190,148 261,148 261,90" fill="var(--navy)"/></svg>
  <div style="position:absolute;left:12px;top:12px;display:flex;align-items:center;gap:4px"><span class="dot gold" style="width:10px;height:10px"></span><span style="font-family:Montserrat,sans-serif;font-weight:700;font-size:7px;color:var(--navy);line-height:1.1">MERIDALE CREST<br>ADVISORS</span></div>
  <div class="title" style="left:11px;top:52px;font-size:9px;font-weight:800">MERIDALE CREST ADVISORS</div>
  <div style="position:absolute;left:11px;top:66px;width:14px;height:1px;background:var(--gold)"></div>
  <div style="position:absolute;left:11px;top:70px;font-family:Montserrat,sans-serif;font-weight:600;font-size:5.5px;color:var(--gold)">Outsourced Franchise Sales &amp; Growth Experts</div>
  <p class="sm" style="position:absolute;left:11px;top:80px;width:100px">Helping franchisors grow faster without the cost and risk of building an internal franchise development team.</p>
</section>

<!-- 02 Index -->
<section class="slide" style="left:325px;top:36px;background:linear-gradient(135deg,#eef2f8,var(--ice))">
  <div class="photo" role="img" aria-label="Faint technical bridge drawing background" style="inset:0;background:linear-gradient(180deg,rgba(255,255,255,.3),rgba(180,195,215,.35))"></div>
  <div class="brand" style="left:8px;right:auto">MERIDALE CREST ADVISORS</div>
  <div class="title" style="left:0;right:0;top:10px;text-align:center">Index</div>
  <div style="position:absolute;left:16px;top:34px;width:230px;display:grid;grid-template-columns:1fr 1fr;column-gap:12px;row-gap:8px">
    <div class="row sm" style="border-bottom:.8px solid var(--gold);padding-bottom:2px"><b style="background:var(--navy);color:#fff;padding:0 2px">1</b>Introduction<span style="margin-left:auto">01</span></div>
    <div class="row sm" style="border-bottom:.8px solid var(--gold);padding-bottom:2px"><b style="background:var(--navy);color:#fff;padding:0 2px">2</b>Index<span style="margin-left:auto">02</span></div>
    <div class="row sm" style="border-bottom:.8px solid var(--gold);padding-bottom:2px"><b style="background:var(--navy);color:#fff;padding:0 2px">3</b>Our Services<span style="margin-left:auto">03</span></div>
    <div class="row sm" style="border-bottom:.8px solid var(--gold);padding-bottom:2px"><b style="background:var(--navy);color:#fff;padding:0 2px">4</b>Why Us<span style="margin-left:auto">04</span></div>
    <div class="row sm" style="border-bottom:.8px solid var(--gold);padding-bottom:2px"><b style="background:var(--navy);color:#fff;padding:0 2px">5</b>How we works<span style="margin-left:auto">05</span></div>
    <div class="row sm" style="border-bottom:.8px solid var(--gold);padding-bottom:2px"><b style="background:var(--navy);color:#fff;padding:0 2px">6</b>How we protect<span style="margin-left:auto">06</span></div>
    <div class="row sm" style="border-bottom:.8px solid var(--gold);padding-bottom:2px"><b style="background:var(--navy);color:#fff;padding:0 2px">7</b>Why partner with us<span style="margin-left:auto">07</span></div>
    <div class="row sm" style="border-bottom:.8px solid var(--gold);padding-bottom:2px"><b style="background:var(--navy);color:#fff;padding:0 2px">8</b>Lets talk with us<span style="margin-left:auto">08</span></div>
    <div class="row sm" style="border-bottom:.8px solid var(--gold);padding-bottom:2px"><b style="background:var(--navy);color:#fff;padding:0 2px">9</b>Our Clients<span style="margin-left:auto">09</span></div>
    <div class="row sm" style="border-bottom:.8px solid var(--gold);padding-bottom:2px"><b style="background:var(--navy);color:#fff;padding:0 2px">10</b>Contact Us<span style="margin-left:auto">10</span></div>
  </div>
  <div class="foot"><span class="url"><svg><use href="#i-globe"/></svg>www.meridalecrestadvisors.example</span><span class="page">Page 02</span></div>
</section>

<!-- 03 Challenge -->
<section class="slide" style="left:617px;top:36px">
  <div class="photo" role="img" aria-label="Stressed founder at a desk in a dim office" style="left:0;top:0;width:96px;height:138px;background:linear-gradient(150deg,#3d3a35,#1a1c22 60%,#6b5236)"></div>
  <svg style="position:absolute;left:0;top:0" width="261" height="148"><polygon points="88,0 98,0 108,138 98,138" fill="var(--gold)"/><polygon points="98,0 261,0 261,138 108,138" fill="#fff"/></svg>
  <div class="brand">MERIDALE CREST ADVISORS</div>
  <div class="title" style="left:120px;top:8px">The Challenge<br><span class="g" style="font-size:7.5px">Facing Emerging Franchisors</span></div>
  <ul class="list sm" style="position:absolute;left:136px;top:40px;display:grid;row-gap:5.5px">
    <li class="row"><span class="dot" style="width:8px;height:8px"><svg><use href="#i-people"/></svg></span>Limited franchise sales resources</li>
    <li class="row"><span class="dot" style="width:8px;height:8px"><svg><use href="#i-gear"/></svg></span>Founder wearing too many hats</li>
    <li class="row"><span class="dot" style="width:8px;height:8px"><svg><use href="#i-chat"/></svg></span>Inconsistent lead follow-up</li>
    <li class="row"><span class="dot" style="width:8px;height:8px"><svg><use href="#i-search"/></svg></span>Difficulty recruiting franchisees</li>
    <li class="row"><span class="dot" style="width:8px;height:8px"><svg><use href="#i-hand"/></svg></span>Lack of broker relationships</li>
    <li class="row"><span class="dot" style="width:8px;height:8px"><svg><use href="#i-dollar"/></svg></span>High cost of internal franchise development staff</li>
  </ul>
  <div class="foot"><span class="url"><svg><use href="#i-globe"/></svg>www.meridalecrestadvisors.example</span><span class="page">Page 03</span></div>
</section>

<!-- 04 Why -->
<section class="slide" style="left:908px;top:36px">
  <div class="brand">MERIDALE CREST ADVISORS</div>
  <div class="title" style="left:9px;top:8px">Why Meridale<br><span class="g">Crest Advisors</span></div>
  <svg style="position:absolute;left:0;top:0" width="261" height="148"><path d="M45,80 A85,70 0 0 1 215,80" fill="none" stroke="var(--navy)" stroke-width="3"/><circle cx="130" cy="32" r="21" fill="#fff" stroke="var(--gold)" stroke-width="1.2"/><use href="#i-trend" x="119" y="21" width="22" height="22" fill="none" stroke="var(--navy)" stroke-width="1.6" stroke-linecap="round" stroke-linejoin="round"/></svg>
  <div style="position:absolute;left:24px;top:76px;width:222px;display:grid;grid-template-columns:repeat(6,1fr);gap:4px">
    <div class="lbl" style="background:#fff;border:.6px solid var(--line);padding:12px 1px 3px;position:relative"><span class="ring" style="position:absolute;left:50%;top:-4px;width:11px;height:11px;margin-left:-5.5px"><svg><use href="#i-people"/></svg></span>Fractional franchise sales team</div>
    <div class="lbl" style="background:#fff;border:.6px solid var(--line);padding:12px 1px 3px;position:relative"><span class="ring" style="position:absolute;left:50%;top:-4px;width:11px;height:11px;margin-left:-5.5px"><svg><use href="#i-building"/></svg></span>30+ years franchise industry experience</div>
    <div class="lbl" style="background:#fff;border:.6px solid var(--line);padding:12px 1px 3px;position:relative"><span class="ring" style="position:absolute;left:50%;top:-4px;width:11px;height:11px;margin-left:-5.5px"><svg><use href="#i-trophy"/></svg></span>500+ franchise sales successes</div>
    <div class="lbl" style="background:#fff;border:.6px solid var(--line);padding:12px 1px 3px;position:relative"><span class="ring" style="position:absolute;left:50%;top:-4px;width:11px;height:11px;margin-left:-5.5px"><svg><use href="#i-clock"/></svg></span>Immediate execution</div>
    <div class="lbl" style="background:#fff;border:.6px solid var(--line);padding:12px 1px 3px;position:relative"><span class="ring" style="position:absolute;left:50%;top:-4px;width:11px;height:11px;margin-left:-5.5px"><svg><use href="#i-gear"/></svg></span>Proven systems and processes</div>
    <div class="lbl" style="background:#fff;border:.6px solid var(--line);padding:12px 1px 3px;position:relative"><span class="ring" style="position:absolute;left:50%;top:-4px;width:11px;height:11px;margin-left:-5.5px"><svg><use href="#i-network"/></svg></span>Deep broker network relationships</div>
  </div>
  <div class="foot"><span class="url"><svg><use href="#i-globe"/></svg>www.meridalecrestadvisors.example</span><span class="page">Page 04</span></div>
</section>

<!-- 05 What takes years -->
<section class="slide" style="left:34px;top:218px">
  <div class="brand">MERIDALE CREST ADVISORS</div>
  <div class="title" style="left:6px;top:8px">What Takes<br>Years to Build,<br><span class="g" style="line-height:1.7">You Get<br>on Day One</span></div>
  <svg style="position:absolute;left:0;top:0" width="261" height="148">
    <circle cx="138" cy="68" r="47" fill="none" stroke="var(--navy)" stroke-width=".8"/>
    <circle cx="138" cy="68" r="21" fill="#fff" stroke="var(--gold)" stroke-width="1.2"/>
    <use href="#i-network" x="127" y="57" width="22" height="22" fill="none" stroke="var(--navy)" stroke-width="1.4" stroke-linecap="round"/>
    <g fill="#fff" stroke="var(--gold)" stroke-width=".8">
      <circle cx="138" cy="21" r="6"/><circle cx="179" cy="45" r="6"/><circle cx="179" cy="91" r="6"/><circle cx="138" cy="115" r="6"/><circle cx="97" cy="91" r="6"/><circle cx="97" cy="45" r="6"/>
    </g>
    <g fill="none" stroke="var(--navy)" stroke-width="2" stroke-linecap="round" stroke-linejoin="round">
      <use href="#i-hand" x="134" y="17" width="8" height="8"/>
      <use href="#i-people" x="175" y="41" width="8" height="8"/>
      <use href="#i-funnel" x="175" y="87" width="8" height="8"/>
      <use href="#i-network" x="134" y="111" width="8" height="8"/>
      <use href="#i-chat" x="93" y="87" width="8" height="8"/>
      <use href="#i-monitor" x="93" y="41" width="8" height="8"/>
    </g>
  </svg>
  <div class="lbl" style="position:absolute;left:146px;top:12px;text-align:left">Franchise broker<br>relationships</div>
  <div class="lbl" style="position:absolute;left:188px;top:41px;text-align:left">Franchise sales<br>expertise</div>
  <div class="lbl" style="position:absolute;left:188px;top:87px;text-align:left">Lead qualification<br>systems</div>
  <div class="lbl" style="position:absolute;left:146px;top:121px;text-align:left">Industry<br>connections</div>
  <div class="lbl" style="position:absolute;left:46px;top:87px;width:42px;text-align:right">Candidate<br>nurturing systems</div>
  <div class="lbl" style="position:absolute;left:46px;top:38px;width:42px;text-align:right">CRM and reporting<br>infrastructure<br>Need ppt<br>design with<br>creativity</div>
  <div class="foot"><span class="url"><svg><use href="#i-globe"/></svg>www.meridalecrestadvisors.example</span><span class="page">Page 05</span></div>
</section>

<!-- 06 Broker community -->
<section class="slide" style="left:325px;top:218px">
  <div class="brand">MERIDALE CREST ADVISORS</div>
  <div class="title" style="left:5px;top:4px">Instant Access<br><span class="g">to the Franchise Broker Community</span></div>
  <div class="sm" style="position:absolute;left:15px;top:31px;font-weight:700">Connecting to:</div>
  <ul class="sm" style="position:absolute;left:22px;top:39px;line-height:2.1;font-size:3.4px">
    <li>Franchise consultants</li><li>Broker networks</li><li>Industry partners</li><li>Referral sources</li><li>Franchise influencers</li>
  </ul>
  <div class="sm" style="position:absolute;left:0;top:88px;width:55px;height:33px;background:var(--navy);color:#fff;font-size:2.6px;padding:3px 3px 3px 16px;line-height:1.3"><span class="dot gold" style="position:absolute;left:3px;top:10px;width:10px;height:10px"><svg><use href="#i-trophy"/></svg></span><b style="color:var(--gold-light)">KEY MESSAGE</b><br>We spent over 20 years building these relationships so your brand doesn't have to.</div>
  <svg style="position:absolute;left:0;top:0" width="261" height="148">
    <g stroke="var(--navy)" stroke-width=".5" stroke-dasharray="1.5 1.5">
      <line x1="175" y1="73" x2="175" y2="30"/><line x1="175" y1="73" x2="225" y2="45"/><line x1="175" y1="73" x2="232" y2="73"/><line x1="175" y1="73" x2="222" y2="102"/><line x1="175" y1="73" x2="175" y2="118"/><line x1="175" y1="73" x2="128" y2="100"/><line x1="175" y1="73" x2="118" y2="73"/><line x1="175" y1="73" x2="128" y2="45"/>
    </g>
    <g fill="var(--navy)"><circle cx="175" cy="42" r="1"/><circle cx="206" cy="56" r="1"/><circle cx="212" cy="73" r="1"/><circle cx="204" cy="91" r="1"/><circle cx="175" cy="104" r="1"/><circle cx="146" cy="90" r="1"/><circle cx="140" cy="73" r="1"/><circle cx="146" cy="56" r="1"/></g>
    <circle cx="175" cy="73" r="20" fill="#fff" stroke="var(--gold)" stroke-width="1"/>
    <g fill="#fff" stroke="var(--line)" stroke-width=".6">
      <rect x="158" y="20" width="34" height="15" rx="2"/><rect x="208" y="38" width="34" height="15" rx="2"/><rect x="215" y="66" width="34" height="15" rx="2"/><rect x="205" y="95" width="34" height="15" rx="2"/><rect x="158" y="112" width="34" height="15" rx="2"/><rect x="112" y="93" width="34" height="15" rx="2"/><rect x="97" y="66" width="34" height="15" rx="2"/><rect x="112" y="38" width="34" height="15" rx="2"/>
    </g>
    <g fill="var(--gold-light)"><rect x="166" y="23" width="18" height="6" rx="1"/><rect x="216" y="41" width="18" height="6" rx="1"/><rect x="223" y="69" width="18" height="6" rx="1"/><rect x="213" y="98" width="18" height="6" rx="1"/><rect x="166" y="115" width="18" height="6" rx="1"/><rect x="120" y="96" width="18" height="6" rx="1"/><rect x="105" y="69" width="18" height="6" rx="1"/><rect x="120" y="41" width="18" height="6" rx="1"/></g>
    <g fill="var(--navy)"><rect x="165" y="31" width="20" height="2.5"/><rect x="215" y="49" width="20" height="2.5"/><rect x="222" y="77" width="20" height="2.5"/><rect x="212" y="106" width="20" height="2.5"/><rect x="165" y="123" width="20" height="2.5"/><rect x="119" y="104" width="20" height="2.5"/><rect x="104" y="77" width="20" height="2.5"/><rect x="119" y="49" width="20" height="2.5"/></g>
  </svg>
  <div style="position:absolute;left:161px;top:65px;font-family:Montserrat,sans-serif;font-weight:700;font-size:3.6px;color:var(--navy);width:28px;text-align:center;line-height:1.15">MERIDALE CREST ADVISORS</div>
  <div class="foot"><span class="url"><svg><use href="#i-globe"/></svg>www.meridalecrestadvisors.example</span><span class="page">Page 06</span></div>
</section>

<!-- 07 Process -->
<section class="slide" style="left:617px;top:218px">
  <div class="brand">MERIDALE CREST ADVISORS</div>
  <div class="title" style="left:0;right:0;top:22px;text-align:center;font-size:7.5px">Our Franchise<br><span class="g">Development Process</span></div>
  <div class="steps">
    <div class="step"><div class="ring"><span class="num">1</span><svg><use href="#i-people"/></svg></div><div class="lbl">Lead</div></div>
    <div class="arrow"><svg viewBox="0 0 6 6"><path d="M1 1l3 2-3 2"/></svg></div>
    <div class="step"><div class="ring"><span class="num">2</span><svg><use href="#i-doc"/></svg></div><div class="lbl">Qualification</div></div>
    <div class="arrow"><svg viewBox="0 0 6 6"><path d="M1 1l3 2-3 2"/></svg></div>
    <div class="step"><div class="ring"><span class="num">3</span><svg><use href="#i-cap"/></svg></div><div class="lbl">Education</div></div>
    <div class="arrow"><svg viewBox="0 0 6 6"><path d="M1 1l3 2-3 2"/></svg></div>
    <div class="step"><div class="ring"><span class="num">4</span><svg><use href="#i-doc"/></svg></div><div class="lbl">FDD Review</div></div>
    <div class="arrow"><svg viewBox="0 0 6 6"><path d="M1 1l3 2-3 2"/></svg></div>
    <div class="step"><div class="ring"><span class="num">5</span><svg><use href="#i-shield"/></svg></div><div class="lbl">Validation</div></div>
    <div class="arrow"><svg viewBox="0 0 6 6"><path d="M1 1l3 2-3 2"/></svg></div>
    <div class="step"><div class="ring"><span class="num">6</span><svg><use href="#i-cal"/></svg></div><div class="lbl">Discovery Day</div></div>
    <div class="arrow"><svg viewBox="0 0 6 6"><path d="M1 1l3 2-3 2"/></svg></div>
    <div class="step"><div class="ring"><span class="num">7</span><svg><use href="#i-hand"/></svg></div><div class="lbl">Franchise<br>Award</div></div>
  </div>
  <div class="foot"><span class="url"><svg><use href="#i-globe"/></svg>www.meridalecrestadvisors.example</span><span class="page">Page 07</span></div>
</section>

<!-- 08 Referral -->
<section class="slide" style="left:908px;top:218px;background:var(--cream)">
  <div class="brand">MERIDALE CREST ADVISORS</div>
  <div class="title" style="left:17px;top:14px">Building a Referral<br><span class="g">Engine for Your Brand</span></div>
  <div class="sm" style="position:absolute;left:17px;top:37px">Focus on broker development:</div>
  <svg style="position:absolute;left:0;top:0" width="261" height="148">
    <circle cx="130" cy="80" r="30" fill="none" stroke="var(--line)" stroke-width="1.5"/>
    <circle cx="130" cy="38" r="14" fill="var(--navy)"/><circle cx="130" cy="115" r="14" fill="var(--navy)"/>
    <circle cx="94" cy="78" r="13" fill="var(--gold)"/><circle cx="166" cy="78" r="13" fill="var(--gold)"/>
    <g fill="none" stroke="#fff" stroke-width="1.6" stroke-linecap="round" stroke-linejoin="round">
      <use href="#i-cap" x="122" y="30" width="16" height="16"/>
      <use href="#i-chat" x="122" y="107" width="16" height="16"/>
      <use href="#i-hand" x="86" y="70" width="16" height="16"/>
      <use href="#i-star" x="158" y="70" width="16" height="16"/>
    </g>
    <g fill="var(--navy)"><circle cx="122" cy="70" r="3"/><circle cx="130" cy="67" r="3.5"/><circle cx="138" cy="70" r="3"/><path d="M116,86 q6,-12 12,0z M124,86 q6,-14 12,0z M132,86 q6,-12 12,0z"/></g>
  </svg>
  <div class="lbl" style="position:absolute;left:148px;top:26px;text-align:left;text-transform:none;font-size:3.4px">Broker/Consultant<br>education</div>
  <div class="lbl" style="position:absolute;left:50px;top:74px;width:28px;text-align:right;text-transform:none;font-size:3.4px">Referral<br>generation</div>
  <div class="lbl" style="position:absolute;left:185px;top:74px;text-align:left;text-transform:none;font-size:3.4px">Brand<br>presentations</div>
  <div class="lbl" style="position:absolute;left:146px;top:120px;text-align:left;text-transform:none;font-size:3.4px">Ongoing<br>communication</div>
  <div class="foot"><span class="url"><svg><use href="#i-globe"/></svg>www.meridalecrestadvisors.example</span><span class="page">Page 08</span></div>
</section>

<!-- 09 Cost comparison -->
<section class="slide" style="left:34px;top:401px">
  <div class="brand">MERIDALE CREST ADVISORS</div>
  <div class="title" style="left:7px;top:6px">The Cost of Hiring vs. Outsourcing</div>
  <div style="position:absolute;left:24px;top:33px;width:86px;border:.6px solid var(--line)">
    <div style="background:var(--navy);color:#fff;font-family:Montserrat,sans-serif;font-weight:700;font-size:3.8px;text-align:center;padding:2px">Internal Franchise<br>Development Director</div>
    <ul class="list sm" style="padding:2px 4px;line-height:2.35">
      <li class="row"><span class="dot" style="width:5px;height:5px"><svg><use href="#i-search"/></svg></span>Recruiting costs</li>
      <li class="row"><span class="dot" style="width:5px;height:5px"><svg><use href="#i-dollar"/></svg></span>Salary</li>
      <li class="row"><span class="dot" style="width:5px;height:5px"><svg><use href="#i-shield"/></svg></span>Benefits</li>
      <li class="row"><span class="dot" style="width:5px;height:5px"><svg><use href="#i-doc"/></svg></span>Payroll taxes</li>
      <li class="row"><span class="dot" style="width:5px;height:5px"><svg><use href="#i-cap"/></svg></span>Training</li>
      <li class="row"><span class="dot" style="width:5px;height:5px"><svg><use href="#i-chart"/></svg></span>Ramp-up period</li>
      <li class="row"><span class="dot" style="width:5px;height:5px"><svg><use href="#i-target"/></svg></span>Unknown performance</li>
    </ul>
  </div>
  <div style="position:absolute;left:117px;top:67px;width:26px;height:26px;border-radius:50%;background:#fff;box-shadow:0 0 4px rgba(0,0,0,.2);font-family:Montserrat,sans-serif;font-weight:700;font-size:8px;color:var(--navy);display:flex;align-items:center;justify-content:center">VS.</div>
  <div style="position:absolute;left:149px;top:33px;width:86px;border:.6px solid var(--line)">
    <div style="background:var(--gold);color:#fff;font-family:Montserrat,sans-serif;font-weight:700;font-size:3.8px;text-align:center;padding:4.2px 2px">Meridale Crest Advisors</div>
    <ul class="list sm" style="padding:2px 4px;line-height:2.35">
      <li class="row"><span class="dot gold" style="width:5px;height:5px"><svg><use href="#i-dollar"/></svg></span>Fractional investment</li>
      <li class="row"><span class="dot gold" style="width:5px;height:5px"><svg><use href="#i-people"/></svg></span>Entire team of experts</li>
      <li class="row"><span class="dot gold" style="width:5px;height:5px"><svg><use href="#i-clock"/></svg></span>Immediate launch</li>
      <li class="row"><span class="dot gold" style="width:5px;height:5px"><svg><use href="#i-gear"/></svg></span>Proven processes</li>
      <li class="row"><span class="dot gold" style="width:5px;height:5px"><svg><use href="#i-hand"/></svg></span>Existing relationships</li>
      <li class="row"><span class="dot gold" style="width:5px;height:5px"><svg><use href="#i-trend"/></svg></span>Scalable growth</li>
    </ul>
  </div>
  <div class="foot"><span class="url"><svg><use href="#i-globe"/></svg>www.meridalecrestadvisors.example</span><span class="page">Page 09</span></div>
</section>

<!-- 10 Services -->
<section class="slide" style="left:325px;top:401px">
  <div class="brand">MERIDALE CREST ADVISORS</div>
  <div class="title" style="left:0;right:0;top:13px;text-align:center">Services <span class="g">We Provide</span></div>
  <div style="position:absolute;left:35px;top:31px;width:200px;display:grid;grid-template-columns:repeat(4,1fr);row-gap:6px">
    <div class="svc"><div class="ring"><svg><use href="#i-search"/></svg></div><div class="lbl">FDD/Operations<br>Review</div></div>
    <div class="svc"><div class="ring"><svg><use href="#i-headset"/></svg></div><div class="lbl">Franchise sales<br>outsourcing</div></div>
    <div class="svc"><div class="ring"><svg><use href="#i-funnel"/></svg></div><div class="lbl">Lead<br>qualification</div></div>
    <div class="svc"><div class="ring"><svg><use href="#i-mail"/></svg></div><div class="lbl">Candidate<br>nurturing</div></div>
    <div class="svc"><div class="ring"><svg><use href="#i-cal"/></svg></div><div class="lbl">Discovery Day<br>coordination</div></div>
    <div class="svc"><div class="ring"><svg><use href="#i-people"/></svg></div><div class="lbl">Broker recruitment /<br>engagement</div></div>
    <div class="svc"><div class="ring"><svg><use href="#i-monitor"/></svg></div><div class="lbl">CRM<br>management</div></div>
    <div class="svc"><div class="ring"><svg><use href="#i-trend"/></svg></div><div class="lbl">Reporting and<br>forecasting</div></div>
  </div>
  <div class="foot"><span class="url"><svg><use href="#i-globe"/></svg>www.meridalecrestadvisors.example</span><span class="page">Page 10</span></div>
</section>

<!-- 11 Experience -->
<section class="slide" style="left:617px;top:401px">
  <div class="photo" role="img" aria-label="Business handshake in front of a bridge and city skyline at dusk" style="left:140px;top:0;width:121px;height:138px;background:linear-gradient(170deg,#2a4a6e,#5a6f86 45%,#c98a4c 80%,#2b2b35);clip-path:ellipse(100% 100% at 100% 50%)"></div>
  <svg style="position:absolute;left:0;top:0" width="261" height="148"><path d="M175,0 Q128,60 150,138" fill="none" stroke="var(--gold)" stroke-width="2.5"/></svg>
  <div class="brand" style="left:8px;right:auto;top:10px">MERIDALE CREST ADVISORS</div>
  <div class="title" style="left:9px;top:30px">Why <span class="g">Experience Matters</span></div>
  <ul class="list" style="position:absolute;left:14px;top:45px;width:110px">
    <li class="row sm" style="border-bottom:.6px solid var(--gold);padding:1.5px 0;font-weight:700;font-size:3.3px;line-height:1.15"><span class="dot" style="width:11px;height:11px"><svg><use href="#i-people"/></svg></span>500+ franchise<br>sales successes</li>
    <li class="row sm" style="border-bottom:.6px solid var(--gold);padding:1.5px 0;font-weight:700;font-size:3.3px;line-height:1.15"><span class="dot" style="width:11px;height:11px"><svg><use href="#i-clock"/></svg></span>30+ years<br>industry experience</li>
    <li class="row sm" style="border-bottom:.6px solid var(--gold);padding:1.5px 0;font-weight:700;font-size:3.3px;line-height:1.15"><span class="dot" style="width:11px;height:11px"><svg><use href="#i-search"/></svg></span>Thousands of franchise<br>candidates evaluated</li>
    <li class="row sm" style="border-bottom:.6px solid var(--gold);padding:1.5px 0;font-weight:700;font-size:3.3px;line-height:1.15"><span class="dot" style="width:11px;height:11px"><svg><use href="#i-hand"/></svg></span>Extensive broker<br>network relationships</li>
    <li class="row sm" style="padding:1.5px 0;font-weight:700;font-size:3.3px;line-height:1.15"><span class="dot" style="width:11px;height:11px"><svg><use href="#i-chart"/></svg></span>Multi-brand franchise<br>development expertise</li>
  </ul>
  <div class="foot"><span class="url"><svg><use href="#i-globe"/></svg>www.meridalecrestadvisors.example</span><span class="page">Page 11</span></div>
</section>

<!-- 12 Success stories -->
<section class="slide" style="left:908px;top:401px">
  <div class="brand">MERIDALE CREST ADVISORS</div>
  <div class="title" style="left:9px;top:12px">Success <span class="g">Stories</span></div>
  <svg style="position:absolute;left:0;top:0" width="261" height="148"><g stroke="var(--gold)" stroke-width=".5"><line x1="80" y1="70" x2="96" y2="64"/><line x1="161" y1="64" x2="178" y2="70"/></g></svg>
  <div style="position:absolute;left:16px;top:52px;width:64px;height:62px;background:#fff;box-shadow:0 0 3px rgba(0,0,0,.15);text-align:center;padding-top:18px">
    <div class="ring navy" style="position:absolute;left:19px;top:-12px;width:26px;height:26px"><svg><use href="#i-gear"/></svg></div>
    <div style="font-family:Montserrat,sans-serif;font-weight:700;font-size:4px">CASE STUDY #1</div>
    <p class="sm" style="font-size:2.9px;padding:1px 3px">Regional fitness brand expanded to new markets, awarding multiple units within its first year of partnership.</p>
  </div>
  <div style="position:absolute;left:97px;top:30px;width:64px;height:62px;background:#fff;box-shadow:0 0 3px rgba(0,0,0,.15);text-align:center;padding-top:18px">
    <div class="ring navy" style="position:absolute;left:19px;top:-12px;width:26px;height:26px"><svg><use href="#i-hand"/></svg></div>
    <div style="font-family:Montserrat,sans-serif;font-weight:700;font-size:4px">CASE STUDY #1</div>
    <p class="sm" style="font-size:2.9px;padding:1px 3px">Emerging food concept built a steady broker pipeline and doubled qualified candidate flow in two quarters.</p>
  </div>
  <div style="position:absolute;left:178px;top:52px;width:64px;height:62px;background:#fff;box-shadow:0 0 3px rgba(0,0,0,.15);text-align:center;padding-top:18px">
    <div class="ring navy" style="position:absolute;left:19px;top:-12px;width:26px;height:26px"><svg><use href="#i-bulb"/></svg></div>
    <div style="font-family:Montserrat,sans-serif;font-weight:700;font-size:4px">CASE STUDY #1</div>
    <p class="sm" style="font-size:2.9px;padding:1px 3px">Home services franchisor replaced an internal hire and lifted annual unit sales with a fractional team model.</p>
  </div>
  <div class="foot"><span class="url"><svg><use href="#i-globe"/></svg>www.meridalecrestadvisors.example</span><span class="page">Page 12</span></div>
</section>

<!-- 13 Enterprise value -->
<section class="slide" style="left:34px;top:583px">
  <div class="brand">MERIDALE CREST ADVISORS</div>
  <div class="title" style="left:5px;top:5px">Building Enterprise Value<br><span class="g">Through Franchise Growth</span></div>
  <div class="sm" style="position:absolute;left:5px;top:29px;font-size:3.1px">Franchise growth creates recurring royalty revenue and increases enterprise value.</div>
  <div style="position:absolute;left:28px;top:46px;width:80px;height:7px;background:var(--navy);color:#fff;font-size:3px;font-weight:700;display:flex;align-items:center;padding-left:14px;border-radius:4px"><span class="ring" style="position:absolute;left:-1px;width:9px;height:9px"><svg><use href="#i-chart"/></svg></span>EXAMPLE GROWTH SCENARIO</div>
  <div style="position:absolute;left:134px;top:46px;width:74px;height:7px;background:var(--navy);color:#fff;font-size:3px;font-weight:700;display:flex;align-items:center;padding-left:14px;border-radius:4px"><span class="ring" style="position:absolute;left:-1px;width:9px;height:9px"><svg><use href="#i-doc"/></svg></span>ILLUSTRATIVE VALUATION RANGE</div>
  <table class="sm" style="position:absolute;left:25px;top:58px;width:95px;border-collapse:collapse;font-size:3px;text-align:center">
    <tr style="background:var(--navy);color:#fff"><th style="padding:1.5px">Stage</th><th>Units</th><th>Annual Royalty Revenue</th></tr>
    <tr style="border-bottom:.5px solid var(--line)"><td style="padding:3.5px 0">Early Growth</td><td>20</td><td>$165,000</td></tr>
    <tr><td style="padding:3.5px 0">Growth Stage</td><td>63</td><td>$1,470,000</td></tr>
  </table>
  <table class="sm" style="position:absolute;left:128px;top:58px;width:100px;border-collapse:collapse;font-size:3px;text-align:center">
    <tr style="background:var(--navy);color:#fff"><th style="padding:1.5px">Royalty Revenue</th><th>10x EBITDA</th><th>15x EBITDA</th></tr>
    <tr style="border-bottom:.5px solid var(--line)"><td style="padding:3.5px 0">$165,000</td><td>$1.65M</td><td>$2.48M</td></tr>
    <tr><td style="padding:3.5px 0">$1,470,000</td><td>$14.7M</td><td>$22.05M</td></tr>
  </table>
  <div style="position:absolute;left:23px;top:99px;width:207px;height:25px;border:.6px solid var(--gold);background:var(--cream);border-radius:2px;display:flex;align-items:center;gap:6px;padding-left:6px">
    <span class="dot" style="width:14px;height:14px;color:var(--gold-light)"><svg><use href="#i-bulb"/></svg></span>
    <b style="font-family:Montserrat,sans-serif;font-size:5px;line-height:1.1;color:var(--navy)">KEY<br>TAKEAWAY</b>
    <p class="sm" style="font-size:3.1px;margin-left:18px">Franchise growth is not just about selling franchises.<br>It is about creating recurring royalty revenue that can<br><i>significantly increase the value of the franchise system.</i></p>
  </div>
  <div class="foot"><span class="url"><svg><use href="#i-globe"/></svg>www.meridalecrestadvisors.example</span><span class="page">Page 13</span></div>
</section>

<!-- 14 Exit -->
<section class="slide" style="left:325px;top:583px;background:linear-gradient(90deg,#fff 40%,var(--cream))">
  <div class="photo" role="img" aria-label="Stylised suspension bridge rising toward a city skyline with a growth arrow" style="left:60px;top:70px;width:110px;height:68px;background:linear-gradient(180deg,rgba(255,255,255,0),#e9dcc6 60%,var(--navy))"></div>
  <svg style="position:absolute;left:0;top:0" width="261" height="148"><path d="M210,120 Q228,90 236,48" fill="none" stroke="var(--gold)" stroke-width="2"/><polygon points="232,46 240,46 237,40" fill="var(--gold)"/></svg>
  <div class="brand">MERIDALE CREST ADVISORS</div>
  <div class="title" style="left:15px;top:19px;font-size:8.5px">Creating Future<br><span class="g">Exit Opportunities</span></div>
  <div class="sm" style="position:absolute;left:15px;top:46px;font-size:5px">Potential outcomes:</div>
  <div class="sm" style="position:absolute;left:15px;top:64px;font-size:5px">Message:</div>
  <p class="sm" style="position:absolute;left:15px;top:72px;width:70px;font-size:3.4px">Every franchise sold today may contribute to enterprise value tomorrow.</p>
  <div style="position:absolute;left:148px;top:28px;font-family:Montserrat,sans-serif;font-size:4px;color:var(--gold);letter-spacing:.3px;font-weight:600">POTENTIAL OUTCOMES:</div>
  <ul class="list sm" style="position:absolute;left:146px;top:39px;width:82px;display:grid;row-gap:3.5px;font-size:3.2px">
    <li class="row" style="background:#fff;box-shadow:0 0 2px rgba(0,0,0,.1)"><span class="dot" style="width:11px;height:11px"><svg><use href="#i-hand"/></svg></span>Private equity acquisition</li>
    <li class="row" style="background:#fff;box-shadow:0 0 2px rgba(0,0,0,.1)"><span class="dot" style="width:11px;height:11px"><svg><use href="#i-building"/></svg></span>Strategic buyer acquisition</li>
    <li class="row" style="background:#fff;box-shadow:0 0 2px rgba(0,0,0,.1)"><span class="dot" style="width:11px;height:11px"><svg><use href="#i-dollar"/></svg></span>Recapitalization</li>
    <li class="row" style="background:#fff;box-shadow:0 0 2px rgba(0,0,0,.1)"><span class="dot" style="width:11px;height:11px"><svg><use href="#i-people"/></svg></span>Family succession</li>
    <li class="row" style="background:#fff;box-shadow:0 0 2px rgba(0,0,0,.1);line-height:1.1"><span class="dot" style="width:11px;height:11px"><svg><use href="#i-chart"/></svg></span>Long-term cash<br>flow ownership</li>
  </ul>
  <div class="foot"><span class="url"><svg><use href="#i-globe"/></svg>www.meridalecrestadvisors.example</span><span class="page">Page 14</span></div>
</section>

<!-- 15 Different -->
<section class="slide" style="left:617px;top:583px">
  <div class="photo" role="img" aria-label="Suspension bridge over a calm bay at sunrise" style="left:120px;top:20px;width:141px;height:118px;background:linear-gradient(180deg,#c9d6e4,#6d8db0 55%,#2c4a6e);clip-path:ellipse(100% 100% at 100% 100%)"></div>
  <svg style="position:absolute;left:0;top:0" width="261" height="148"><path d="M120,138 Q150,40 261,22" fill="none" stroke="var(--navy)" stroke-width="5"/><path d="M126,138 Q156,46 261,28" fill="none" stroke="var(--gold)" stroke-width="1.5"/></svg>
  <div class="brand">MERIDALE CREST ADVISORS</div>
  <div class="title" style="left:5px;top:4px;font-size:8.5px">Why Meridale Crest<br><span class="g">Advisors Is Different</span></div>
  <ul class="list sm" style="position:absolute;left:7px;top:36px;width:105px;font-weight:700;font-size:3.4px">
    <li class="row" style="border-bottom:.5px solid var(--line);padding:1.3px 0"><span class="dot" style="width:8px;height:8px"><svg><use href="#i-dollar"/></svg></span>|&nbsp;Fractional cost model</li>
    <li class="row" style="border-bottom:.5px solid var(--line);padding:1.3px 0"><span class="dot" style="width:8px;height:8px"><svg><use href="#i-clock"/></svg></span>|&nbsp;Immediate execution</li>
    <li class="row" style="border-bottom:.5px solid var(--line);padding:1.3px 0"><span class="dot" style="width:8px;height:8px"><svg><use href="#i-trophy"/></svg></span>|&nbsp;550+ franchise sales</li>
    <li class="row" style="border-bottom:.5px solid var(--line);padding:1.3px 0"><span class="dot" style="width:8px;height:8px"><svg><use href="#i-check"/></svg></span>|&nbsp;30+ years' experience</li>
    <li class="row" style="border-bottom:.5px solid var(--line);padding:1.3px 0"><span class="dot" style="width:8px;height:8px"><svg><use href="#i-network"/></svg></span>|&nbsp;Established broker network</li>
    <li class="row" style="border-bottom:.5px solid var(--line);padding:1.3px 0"><span class="dot" style="width:8px;height:8px"><svg><use href="#i-gear"/></svg></span>|&nbsp;Proven franchise growth systems</li>
    <li class="row" style="padding:1.3px 0"><span class="dot" style="width:8px;height:8px"><svg><use href="#i-target"/></svg></span>|&nbsp;Strategic growth partner</li>
  </ul>
  <div class="foot"><span class="url"><svg><use href="#i-globe"/></svg>www.meridalecrestadvisors.example</span><span class="page">Page 15</span></div>
</section>

<!-- 16 Engagement -->
<section class="slide" style="left:908px;top:583px;background:linear-gradient(135deg,#f3f6fa,#e4ebf3)">
  <div class="brand">MERIDALE CREST ADVISORS</div>
  <div class="title" style="left:19px;top:33px">Engagement <span class="g">Options</span></div>
  <ul class="sm" style="position:absolute;left:24px;top:58px;font-size:4px;line-height:2.2;list-style:none">
    <li><span style="color:var(--gold)">•</span> Franchise Sales Outsourcing</li><li><span style="color:var(--gold)">•</span> Broker Network Development</li><li><span style="color:var(--gold)">•</span> Franchise Growth Consulting</li><li><span style="color:var(--gold)">•</span> Franchise Expansion Strategy</li><li><span style="color:var(--gold)">•</span> Franchise Development Advisory Services</li>
  </ul>
  <svg style="position:absolute;left:0;top:0" width="261" height="148">
    <circle cx="198" cy="75" r="44" fill="var(--navy)" stroke="var(--gold)" stroke-width="2"/>
    <circle cx="198" cy="75" r="31" fill="none" stroke="var(--gold)" stroke-width=".5" stroke-dasharray="2 2"/>
    <g fill="var(--navy)" stroke="var(--gold-light)" stroke-width=".7"><circle cx="198" cy="44" r="7"/><circle cx="170" cy="62" r="7"/><circle cx="226" cy="62" r="7"/><circle cx="177" cy="96" r="7"/><circle cx="219" cy="96" r="7"/></g>
    <g fill="none" stroke="#fff" stroke-width="1.8" stroke-linecap="round" stroke-linejoin="round">
      <use href="#i-chart" x="193" y="39" width="10" height="10"/>
      <use href="#i-people" x="165" y="57" width="10" height="10"/>
      <use href="#i-doc" x="221" y="57" width="10" height="10"/>
      <use href="#i-target" x="172" y="91" width="10" height="10"/>
      <use href="#i-gear" x="214" y="91" width="10" height="10"/>
    </g>
    <use href="#i-hand" x="184" y="61" width="28" height="28" fill="none" stroke="var(--gold-light)" stroke-width="1.3" stroke-linecap="round" stroke-linejoin="round"/>
  </svg>
  <div class="foot"><span class="url"><svg><use href="#i-globe"/></svg>www.meridalecrestadvisors.example</span><span class="page">Page 16</span></div>
</section>

<!-- 17 Closing -->
<section class="slide" style="left:466px;top:762px">
  <div class="photo" role="img" aria-label="Suspension bridge tower at sunset framed in an arch" style="left:150px;top:0;width:111px;height:148px;background:linear-gradient(180deg,#e7b278,#b7764a 45%,#3a2e2a);clip-path:ellipse(95% 100% at 100% 50%)"></div>
  <svg style="position:absolute;left:0;top:0" width="261" height="148"><path d="M170,0 Q128,74 170,148" fill="none" stroke="var(--navy)" stroke-width="7"/><path d="M164,0 Q122,74 164,148" fill="none" stroke="var(--gold)" stroke-width="1"/><path d="M200,140 Q230,130 248,112" fill="none" stroke="var(--gold)" stroke-width="1.2"/></svg>
  <div style="position:absolute;left:17px;top:12px;display:flex;align-items:center;gap:3px"><span class="dot gold" style="width:8px;height:8px"></span><span style="font-family:Montserrat,sans-serif;font-weight:700;font-size:5.5px;color:var(--navy);line-height:1.1">MERIDALE CREST<br>ADVISORS</span></div>
  <div class="title" style="left:18px;top:53px;font-size:12px;line-height:1.15">Let's Build Your<br><span class="g" style="font-size:13px">Growth Plan</span></div>
  <div style="position:absolute;left:18px;top:87px;width:95px;height:17px;background:var(--navy);color:#fff;border-radius:2px;display:flex;align-items:center;gap:4px;padding-left:4px;font-family:Montserrat,sans-serif;font-weight:600;font-size:4.3px;line-height:1.2"><span class="dot gold" style="width:8px;height:8px"><svg><use href="#i-cal"/></svg></span>Schedule a Franchise Growth<br>Strategy Consultation</div>
  <div style="position:absolute;left:18px;top:115px;display:flex;gap:4px;align-items:center">
    <span class="ring navy" style="width:11px;height:11px"><svg><use href="#i-globe"/></svg></span>
    <div style="border-left:.6px solid var(--gold);padding-left:4px;font-size:3.6px;line-height:1.35"><span style="color:var(--gold);font-family:Montserrat,sans-serif;font-weight:600">CONTACT INFORMATION</span><br>Website:<br><b>Meridale Crest Advisors</b></div>
  </div>
</section>

</body>
</html>
```